Web Design Project

We need a website design for our marketing agency: loftwaveo.com.au

We want something that is eye-catching and will wow audiences, yet at the same time it cannot turn-off corporate clients. The website should be highly focused on conversions with numerous call to actions on each page.

We like blue as our primary colour and have a mascot (the spider on the current website)

Target Market(s)

small business owners
small corporations
enterprise level business clients

Industry/Entity Type

Marketing

Requirements
Must have
• must incorporate the agency mascot (the spider on the website)

```html
<!DOCTYPE html>
<html lang="en">
<head>
<meta charset="utf-8">
<title>Loftwaveo – High ROI Digital Marketing</title>
<link href="https://fonts.googleapis.com/css2?family=Arimo:wght@400;700&family=Open+Sans:wght@600&family=Questrial&display=swap" rel="stylesheet">
<style>
:root{
  --ink:#3a3a3a;
  --muted:#6b6b6b;
  --blue:#3f79d4;
  --blue-dark:#2a5fb8;
  --blue-light:#6fa0e6;
  --hero-top:#3f76cf;
  --hero-bottom:#75a4e8;
  --card-bg:#efefef;
  --line:#d5d5d5;
  --white:#ffffff;
}
*{box-sizing:border-box;margin:0;padding:0}
html,body{width:1127px;height:1200px;overflow:hidden;background:var(--white);font-family:"Arimo",Arial,sans-serif;color:var(--ink)}
.page{position:relative;width:1127px;height:1200px}

/* Header */
.site-header{position:absolute;left:0;top:0;width:1127px;height:84px;background:linear-gradient(#ffffff,#f1f1f1)}
.brand{position:absolute;left:135px;top:12px;display:flex;align-items:center;gap:10px}
.brand-name{font-family:"Arimo",Arial,sans-serif;font-weight:700;font-size:40px;letter-spacing:1px;color:var(--ink);text-transform:uppercase}
.brand-dot{width:30px;height:30px;border-radius:50%;background:var(--blue)}
.tagline{position:absolute;left:137px;top:59px;font-size:11px;color:var(--muted);letter-spacing:.3px}
.contact{position:absolute;right:135px;top:4px;width:245px;font-size:12px;line-height:15px;color:var(--ink)}
.contact-row{display:flex;gap:4px}
.contact-label{color:var(--blue);font-size:14px;white-space:nowrap}
.contact-phone{margin-top:6px;align-items:center}
.contact svg{flex:none}

/* Navigation */
.main-nav{position:absolute;left:0;top:84px;width:1127px;height:36px;background:linear-gradient(#f4f4f4,#e6e6e6);border-top:1px solid #d8d8d8;border-bottom:1px solid #cfcfcf}
.main-nav a{position:absolute;top:9px;transform:translateX(-50%);font-family:"Open Sans",Arial,sans-serif;font-weight:600;font-size:13.5px;color:#333;text-decoration:none;white-space:nowrap}
.main-nav a.active{top:4px;padding:3px 11px;border:1px solid #c9c9c9;border-radius:4px;background:#fff;color:var(--blue)}

/* Hero */
.hero{position:absolute;left:0;top:120px;width:1127px;height:341px;background:linear-gradient(var(--hero-top),var(--hero-bottom));border-top:2px solid #5b8fe0;border-bottom:2px dashed #5d8ed8}
.hero-arrow{position:absolute;top:156px}
.hero-copy{position:absolute;left:209px;top:58px;width:280px;color:var(--white)}
.hero-title{font-family:"Questrial",Arial,sans-serif;font-weight:400;font-size:26px;letter-spacing:.3px;text-shadow:0 1px 2px rgba(0,0,0,.25)}
.hero-text{margin-top:12px;font-size:12px;line-height:21px}
.signup{position:absolute;left:211px;top:255px;width:172px;height:44px;border:2px solid #cfe1fb;border-radius:10px;background:linear-gradient(#8fb8f0,#4f85d9);color:var(--white);font-family:"Questrial",Arial,sans-serif;font-size:22px;display:flex;align-items:center;justify-content:center;box-shadow:0 2px 4px rgba(0,0,0,.25)}
.laptop{position:absolute;left:537px;top:60px}

/* Service cards */
.services{position:absolute;left:135px;top:484px;width:857px;display:grid;grid-template-columns:repeat(4,194px);column-gap:27px;row-gap:19px}
.card{height:269px;background:linear-gradient(#ffffff,var(--card-bg));border:1px solid var(--line);padding:2px;box-shadow:0 1px 2px rgba(0,0,0,.12)}
.card-title{height:38px;background:linear-gradient(#4f88dc,var(--blue-dark));color:var(--white);font-weight:700;font-size:13px;display:flex;align-items:center;justify-content:center;text-shadow:0 1px 1px rgba(0,0,0,.3);white-space:nowrap}
.card-art{width:90px;height:82px;margin:8px auto 10px;border-radius:14px}
.card-text{padding:0 4px 0 5px;font-size:9.6px;line-height:15.8px;color:#333}
.art-ad{background:linear-gradient(135deg,#d9534a,#3d6fb8)}
.art-seo{background:radial-gradient(circle,#4f8fe0,#9aa6b3)}
.art-social{background:radial-gradient(circle,#f0c340,#4aa84a 60%,#d94a3a)}
.art-chart{background:linear-gradient(90deg,#f39a2b,#4a7de0,#41c24a)}
.art-search{background:linear-gradient(135deg,#e8e8e8,#6b8fc9)}
.art-growth{background:linear-gradient(0deg,#2f6fd0,#5cbf3c,#e64a3a)}
.art-cycle{background:radial-gradient(circle,#d9a63a,#7aa93a 55%,#cf3b30)}
.art-arrows{background:linear-gradient(135deg,#3fa0e8,#e03a3a,#f0b03a)}

/* Footer */
.site-footer{position:absolute;left:0;top:1067px;width:1127px;height:133px;background:linear-gradient(var(--blue),#4b82d8);border-top:4px solid #d6e3f6}
.footer-brand{position:absolute;left:132px;top:24px;display:flex;align-items:center;gap:10px}
.footer-brand .brand-name{color:#8cb1ea;font-size:36px}
.footer-brand .brand-dot{background:#8cb1ea}
.footer-tagline{position:absolute;left:212px;top:64px;font-size:8.5px;letter-spacing:.8px;color:#9dbced}
.footer-rule{position:absolute;left:134px;top:88px;width:858px;height:1px;background:#8cb0e6}
.copyright{position:absolute;left:134px;top:101px;font-size:9.5px;color:var(--white)}
.footer-nav{position:absolute;right:135px;top:98px;font-size:9.5px;color:var(--white);display:flex;gap:7px}
.footer-nav a{color:var(--white);text-decoration:none}
</style>
</head>
<body>
<div class="page">

<header class="site-header">
  <div class="brand"><span class="brand-name">Loftwaveo</span><span class="brand-dot"></span></div>
  <div class="tagline">HIGH ROI DIGITAL MARKETING</div>
  <div class="contact">
    <div class="contact-row">
      <svg width="12" height="14" viewBox="0 0 12 14"><rect x="1" y="1" width="10" height="12" rx="1" fill="#ddd" stroke="#777"/><rect x="3" y="4" width="6" height="1.5" fill="#777"/><rect x="3" y="7" width="6" height="1.5" fill="#777"/></svg>
      <span class="contact-label">Address :</span>
      <span>Level 12, Harbourline Tower, 48 Kestrel Street, Brisbane, Qld, 4000</span>
    </div>
    <div class="contact-row contact-phone">
      <svg width="16" height="16" viewBox="0 0 16 16"><circle cx="8" cy="8" r="7" fill="#5cb83a"/><path d="M5 4h2l1 2-1 1a6 6 0 0 0 2 2l1-1 2 1v2c-4 0-7-3-7-7z" fill="#fff"/></svg>
      <span class="contact-label">Call Us Now :</span>
      <span>(+617) 3555 0148</span>
    </div>
  </div>
</header>

<nav class="main-nav">
  <a class="active" style="left:166px">Home</a>
  <a style="left:259px">Services</a>
  <a style="left:368px">Blog</a>
  <a style="left:487px">SEO Pricing</a>
  <a style="left:605px">SEM</a>
  <a style="left:736px">About Loftwaveo</a>
  <a style="left:911px">Contact Loftwaveo</a>
</nav>

<section class="hero">
  <svg class="hero-arrow" style="left:137px" width="32" height="34" viewBox="0 0 32 34"><path d="M26 3 L8 17 L26 31" fill="none" stroke="#fff" stroke-width="6" stroke-linejoin="round"/></svg>
  <svg class="hero-arrow" style="left:957px" width="32" height="34" viewBox="0 0 32 34"><path d="M6 3 L24 17 L6 31" fill="none" stroke="#fff" stroke-width="6" stroke-linejoin="round"/></svg>

  <div class="hero-copy">
    <h1 class="hero-title">Example Slider Page 1</h1>
    <p class="hero-text">Lorem ipsum dolor sit amet, consectetur adipiscing elit. Integer dictum, neque ut imperdiet pellentesque, nulla tellus tempus magna, sed consectetur orci metus a justo. Aliquam ac congue nunc. Mauris a tortor ut massa egestas tempus.</p>
  </div>
  <div class="signup">Sign Up</div>

  <svg class="laptop" width="444" height="242" viewBox="0 0 444 242">
    <defs>
      <linearGradient id="base" x1="0" y1="0" x2="0" y2="1"><stop offset="0" stop-color="#f2f2f2"/><stop offset="1" stop-color="#8e8e8e"/></linearGradient>
      <linearGradient id="screen" x1="0" y1="0" x2="0" y2="1"><stop offset="0" stop-color="#e4ecf8"/><stop offset=".3" stop-color="#7fb0ea"/><stop offset=".45" stop-color="#f7f9fc"/><stop offset="1" stop-color="#ffffff"/></linearGradient>
    </defs>
    <rect x="56" y="0" width="330" height="220" rx="8" fill="#111" stroke="#555"/>
    <rect x="70" y="25" width="303" height="179" fill="url(#screen)" role="img" aria-label="Screenshot of the agency's campaign dashboard"/>
    <rect x="0" y="218" width="444" height="14" rx="3" fill="url(#base)"/>
    <rect x="190" y="218" width="64" height="4" rx="2" fill="#9a9a9a"/>
    <circle cx="224" cy="100" r="63" fill="#a9c6ea"/>
    <circle cx="224" cy="100" r="53" fill="#ffffff"/>
    <path d="M211 77 L244 100 L211 123 Z" fill="#2e9ca6"/>
    <text x="225" y="185" text-anchor="middle" font-family="Arimo, Arial, sans-serif" font-size="16" fill="#5c93d8">Watch a Video</text>
  </svg>
</section>

<main class="services">
  <article class="card">
    <h2 class="card-title">Online Ad Management</h2>
    <div class="card-art art-ad" role="img" aria-label="Illustration of an advertising billboard"></div>
    <p class="card-text">Need highly targeted traffic right now? Then let us help! We have a whole range of online advertising solutions, from Searchly Promote to Friendbook Ads to interactive banner Ads. Ad copy, creatives design &amp; conversion optimization – we can handle everything and get you the highest ROI for your ad dollar.</p>
  </article>
  <article class="card">
    <h2 class="card-title">SEO Packages</h2>
    <div class="card-art art-seo" role="img" aria-label="Illustration of the spider mascot with a magnifying glass"></div>
    <p class="card-text">Drive quality traffic to your business and boost your revenue. We offer high quality SEO packages at competitive rates with GUARANTEED results. Whether you're a local business or a national enterprise, we can help your business grow.</p>
  </article>
  <article class="card">
    <h2 class="card-title">Social Media</h2>
    <div class="card-art art-social" role="img" aria-label="Illustration of a connected social network"></div>
    <p class="card-text">Need to engage your target market? Want build your brand to create a loyal base of supporters for your business? Then social media is your solution. We can advise which social media options are right for your business – and there are way more options than just Friendbook and Chirper!</p>
  </article>
  <article class="card">
    <h2 class="card-title">Loftwaveo Digital Marketing</h2>
    <div class="card-art art-chart" role="img" aria-label="Illustration of a colourful bar chart with a magnifier"></div>
    <p class="card-text">Online marketing channels are a major factor almost any business. Loftwaveo is a digital marketing agency focused on results and ROI. Whether its search engine optimisation with our advanced SEO services or Pay-Per-Click search engine marketing (SEM)...</p>
  </article>

  <article class="card">
    <h2 class="card-title">Search Engine Optimisation</h2>
    <div class="card-art art-search" role="img" aria-label="Illustration of SEO letter blocks"></div>
    <p class="card-text">Need highly targeted traffic right now? Then let us help! We have a whole range of online advertising solutions, from Searchly Promote to Friendbook Ads to interactive banner Ads. Ad copy, creatives design &amp; conversion optimization – we can handle everything and get you the highest ROI for your ad dollar.</p>
  </article>
  <article class="card">
    <h2 class="card-title">SEO Services</h2>
    <div class="card-art art-growth" role="img" aria-label="Illustration of rising arrows over an SEO label"></div>
    <p class="card-text">Drive quality traffic to your business and boost your revenue. We offer high quality SEO packages at competitive rates with GUARANTEED results. Whether you're a local business or a national enterprise, we can help your business grow.</p>
  </article>
  <article class="card">
    <h2 class="card-title">SEO Brisbane</h2>
    <div class="card-art art-cycle" role="img" aria-label="Illustration of interlocking gears for presence, traffic and conversion"></div>
    <p class="card-text">Need to engage your target market? Want build your brand to create a loyal base of supporters for your business? Then social media is your solution. We can advise which social media options are right for your business – and there are way more options than just Friendbook and Chirper!</p>
  </article>
  <article class="card">
    <h2 class="card-title">SEM Services</h2>
    <div class="card-art art-arrows" role="img" aria-label="Illustration of arrows rising from a dollar sign"></div>
    <p class="card-text">Online marketing channels are a major factor almost any business. Loftwaveo is a digital marketing agency focused on results and ROI. Whether its search engine optimisation with our advanced SEO services or Pay-Per-Click search engine marketing (SEM)...</p>
  </article>
</main>

<footer class="site-footer">
  <div class="footer-brand"><span class="brand-dot"></span><span class="brand-name">Loftwaveo</span></div>
  <div class="footer-tagline">HIGH ROI DIGITAL MARKETING</div>
  <div class="footer-rule"></div>
  <p class="copyright">© 2011 Loftwaveo. All Rights Reserved</p>
  <nav class="footer-nav">
    <a>Home</a><span>|</span><a>Services</a><span>|</span><a>Blog</a><span>|</span><a>SEO Pricing</a><span>|</span><a>SEM</a><span>|</span><a>About Loftwaveo</a><span>|</span><a>Contact Loftwaveo</a>
  </nav>
</footer>

</div>
</body>
</html>
```